Harbourline Gas and Plumbing Business Card Design

I am after a business card design for my plumbing business called 'Harbourline Gas & Plumbing'. I do all types of plumbing and gas work and specialise in general maintenance plumbing. Would like to see designs using current logo

Industry/Entity Type

Plumbing

Contact Information for Business Card

Name - Dallas McTavish
Phone number - 0468305917
Email - admin@harbourlinegasandplumbing.com.au
ABN - 58104629375

```html
<!DOCTYPE html>
<html lang="en">
<head>
<meta charset="utf-8">
<title>Harbourline Gas &amp; Plumbing – Business Card</title>
<link rel="stylesheet" href="https://fonts.googleapis.com/css2?family=Roboto:wght@400;700;900&family=Roboto+Condensed:wght@700&display=swap">
<style>
  :root {
    --stage: #1c1c1e;
    --blue-deep: #2b3a93;
    --blue-mid: #1f5aa8;
    --blue-bright: #0f76bb;
    --paper-light: #f6f6f6;
    --paper-shade: #e7e7e7;
    --orange: #e8891c;
    --navy: #2c3a8f;
    --ink: #4a4a4a;
    --title-blue: #2d4b9a;
  }
  * { box-sizing: border-box; margin: 0; padding: 0; }
  html, body { width: 1200px; height: 900px; overflow: hidden; }
  body {
    background: var(--stage);
    position: relative;
    font-family: "Roboto", Arial, sans-serif;
  }
  .card {
    position: absolute;
    left: 332px;
    width: 555px;
    height: 317px;
    overflow: hidden;
    box-shadow: 0 10px 24px rgba(0,0,0,.55);
  }
  .card-front {
    top: 134px;
    background: linear-gradient(125deg, var(--blue-deep) 0%, var(--blue-mid) 45%, var(--blue-bright) 62%, var(--blue-mid) 80%, var(--blue-deep) 100%);
    display: flex;
    align-items: center;
    justify-content: center;
  }
  .brand {
    display: flex;
    align-items: center;
    gap: 12px;
    font-weight: 900;
    text-transform: uppercase;
    white-space: nowrap;
  }
  .brand-mark { display: block; }
  .card-front .brand { color: #fff; font-size: 26px; letter-spacing: .5px; }
  .card-front .brand-mark { width: 26px; height: 26px; background: #fff; }

  .card-back {
    top: 488px;
    background: linear-gradient(120deg, var(--paper-light) 0%, var(--paper-shade) 55%, var(--paper-light) 100%);
  }
  .card-back .brand {
    position: absolute;
    left: 39px;
    top: 58px;
    color: var(--navy);
    font-size: 19px;
    letter-spacing: .3px;
    gap: 9px;
  }
  .card-back .brand-mark { width: 19px; height: 19px; background: var(--navy); }
  .accent-marker {
    position: absolute;
    left: 0; top: 175px;
    width: 14px; height: 38px;
    background: var(--navy);
  }
  .person-name {
    position: absolute;
    left: 39px; top: 171px;
    font-family: "Roboto Condensed", "Roboto", sans-serif;
    font-weight: 700;
    font-size: 23px;
    color: var(--title-blue);
  }
  .person-role {
    position: absolute;
    left: 39px; top: 196px;
    font-size: 15px;
    color: var(--ink);
  }
  .contact-list {
    position: absolute;
    left: 39px; top: 228px;
    list-style: none;
    font-size: 13px;
    color: var(--ink);
    letter-spacing: .2px;
  }
  .contact-list li { display: flex; align-items: center; gap: 7px; height: 19px; }
  .contact-list svg { width: 12px; height: 12px; fill: var(--orange); flex: none; }
  .footer-band { position: absolute; left: 0; bottom: 0; width: 555px; height: 29px; }
  .site-url {
    position: absolute;
    left: 308px; bottom: 7px;
    font-size: 13px;
    color: #fff;
    letter-spacing: .2px;
  }
</style>
</head>
<body>
  <section class="card card-front" aria-label="Card front">
    <div class="brand"><span class="brand-mark"></span>Harbourline Gas &amp; Plumbing</div>
  </section>

  <section class="card card-back" aria-label="Card back">
    <div class="brand"><span class="brand-mark"></span>Harbourline Gas &amp; Plumbing</div>

    <span class="accent-marker"></span>
    <h1 class="person-name">Dallas McTavish</h1>
    <p class="person-role">Owner</p>

    <ul class="contact-list">
      <li>
        <svg viewBox="0 0 24 24" aria-hidden="true"><path d="M6.6 10.8a15.1 15.1 0 0 0 6.6 6.6l2.2-2.2a1 1 0 0 1 1-.25 11.4 11.4 0 0 0 3.6.57 1 1 0 0 1 1 1V20a1 1 0 0 1-1 1A17 17 0 0 1 3 4a1 1 0 0 1 1-1h3.5a1 1 0 0 1 1 1c0 1.25.2 2.45.57 3.57a1 1 0 0 1-.25 1z"/></svg>
        0468305917
      </li>
      <li>
        <svg viewBox="0 0 24 24" aria-hidden="true"><path d="M2 5h20v2.2l-10 6-10-6z M2 9.5l10 6 10-6V19H2z"/></svg>
        admin@harbourlinegasandplumbing.com.au
      </li>
    </ul>

    <svg class="footer-band" viewBox="0 0 555 29" aria-hidden="true">
      <polygon points="0,16 280,16 272,29 0,29" fill="var(--orange)"/>
      <polygon points="295,0 555,0 555,29 276,29" fill="var(--navy)"/>
    </svg>
    <span class="site-url">www.harbourlinegasandplumbing.com.au</span>
  </section>
</body>
</html>
```